I need a business card representing my company, VELDRA, it's an artist management and design company. Complete name is "VELDRA Artist Mgmt. + Design Co." I need it to be world class and very appealing, sophisticated and artistically unique.
Updates

Posted an updated Brief please see. I need a business card representing my company, VELDRA, it's an artist management and design company. Complete name is "VELDRA Artist Mgmt. + Design Co." I need it to be world class and very appealing, sophisticated and artistically unique.

Designs look the same

Designs look the same

Target Market(s)

Advertisers, Entertainment Companies, Commercial companies

Industry/Entity Type

Advertising

Contact Information for Business Card

I need a business card representing my company, VELDRA, it's an artist management and design company. Complete name is "VELDRA Artist Mgmt. + Design Co." I need it to be world class and very appealing, sophisticated and artistically unique. One side can be VELDRA Artist Mgmt. + Design Co. and the other my name, Teodoro Lindqvist, my contact telephone: 412.638.2957, email veldraartist@plumora.net, my address: 3264 Harwell Ave. #517 Miami, FL 33184

Font styles to use
Other font styles liked:
• Calibri

Colors
ffffff
0455a3
f37122

Requirements
Must have
• "VELDRA" stand out bigger than the rest of the text.
Nice to have
• Name "VELDRA" can be centered on one side or in the corner or along side edges, just need something cool and different.
Should not have
• I am open just try to keep it clean looking

```html
<!DOCTYPE html>
<html lang="en">
<head>
<meta charset="utf-8">
<title>VELDRA Artist Mgmt. + Design Co. — Business Card</title>
<link href="https://fonts.googleapis.com/css2?family=Questrial&display=swap" rel="stylesheet">
<style>
  :root {
    --bg: #e4e4e2;
    --black: #0b0b0b;
    --white: #ffffff;
    --orange: #e8893a;
    --blue: #0455a3;
    --gold: #a38a4e;
    --gold-dark: #7a6642;
    --brown: #6b5637;
    --grey: #b8b8b8;
    --ink: #2a2a2a;
    --soft: #d6d6d6;
  }
  * { margin: 0; padding: 0; box-sizing: border-box; }
  html, body { width: 1200px; height: 902px; overflow: hidden; }
  body {
    background: var(--bg);
    font-family: "Questrial", "Century Gothic", sans-serif;
    position: relative;
  }
  .card {
    position: absolute;
    left: 250px;
    width: 700px;
    height: 400px;
    border-radius: 22px;
    overflow: hidden;
    box-shadow: 0 6px 18px rgba(0,0,0,.18);
  }
  .card-front { top: 34px; background: var(--black); }
  .card-back  { top: 468px; background: var(--white); }

  /* front */
  .front-brand {
    position: absolute; left: 0; right: 0; top: 130px;
    display: flex; justify-content: center; align-items: center; gap: 16px;
  }
  .brand-square { width: 34px; height: 34px; background: var(--orange); }
  .brand-name {
    color: var(--orange); font-size: 72px; letter-spacing: 4px; line-height: 1;
  }
  .front-tagline {
    position: absolute; left: 0; right: 0; top: 236px;
    text-align: center; color: var(--soft); font-size: 25px; letter-spacing: 1px;
  }

  /* back */
  .name-band {
    position: absolute; left: 0; top: 112px; height: 62px; width: 390px;
    display: flex;
  }
  .name-band .accent { width: 44px; background: var(--orange); }
  .name-band .plate {
    flex: 1; background: var(--gold); position: relative;
    padding: 10px 0 0 18px; color: var(--white);
  }
  .person-name { font-size: 21px; letter-spacing: 2px; line-height: 1.1; white-space: nowrap; }
  .person-email { font-size: 14px; letter-spacing: .5px; margin-top: 3px; white-space: nowrap; }
  .plate .dot {
    position: absolute; right: 18px; top: 22px; width: 16px; height: 16px;
    border-radius: 50%; background: var(--blue);
  }

  .back-brand {
    position: absolute; right: 40px; top: 40px;
    display: flex; align-items: center; gap: 10px;
  }
  .back-brand .brand-square { width: 22px; height: 22px; background: var(--orange); }
  .back-brand .brand-name { color: var(--gold-dark); font-size: 48px; letter-spacing: 3px; }

  .address {
    position: absolute; right: 40px; top: 112px; text-align: right;
    color: var(--ink); font-size: 16px; line-height: 1.35; font-style: normal;
  }
  .address .number { font-size: 34px; color: var(--blue); line-height: 1.1; }

  .contacts {
    position: absolute; left: 40px; top: 236px; list-style: none;
  }
  .contacts li {
    display: flex; align-items: center; gap: 14px; height: 30px; margin-bottom: 4px;
    color: var(--ink); font-size: 17px; letter-spacing: .5px;
  }
  .icon { width: 26px; height: 26px; display: flex; align-items: center; justify-content: center; }
  .icon-office { background: var(--gold); }
  .icon-direct { background: var(--brown); }
  .icon-fax { background: var(--grey); }

  .footer-bands {
    position: absolute; left: 0; right: 0; top: 352px; height: 24px; display: flex;
  }
  .band-grey { width: 210px; background: var(--grey); }
  .band-orange {
    width: 300px; background: var(--orange); color: var(--white);
    display: flex; align-items: center; gap: 8px; padding-left: 60px;
    font-size: 14px; letter-spacing: 6px;
  }
  .band-gold { flex: 1; background: linear-gradient(90deg, var(--gold), var(--gold-dark)); }
  .footer-rule {
    position: absolute; left: 0; width: 210px; top: 384px; height: 16px; background: var(--soft);
  }
</style>
</head>
<body>

<section class="card card-front" aria-label="Card front">
  <div class="front-brand">
    <span class="brand-square"></span>
    <span class="brand-name">veldra</span>
  </div>
  <p class="front-tagline">Artist Management + Design Co.</p>
</section>

<section class="card card-back" aria-label="Card back">
  <div class="name-band">
    <span class="accent"></span>
    <div class="plate">
      <p class="person-name">TEODORO LINDQVIST</p>
      <p class="person-email">veldraartist@plumora.net</p>
      <span class="dot"></span>
    </div>
  </div>

  <div class="back-brand">
    <span class="brand-square"></span>
    <span class="brand-name">veldra</span>
  </div>

  <address class="address">
    <div class="number">3264</div>
    Harwell Avenue<br>
    Studio 517<br>
    Miami, Florida 33184
  </address>

  <ul class="contacts">
    <li>
      <span class="icon icon-office">
        <svg width="16" height="16" viewBox="0 0 24 24"><path fill="#fff" d="M6.6 10.8a15 15 0 0 0 6.6 6.6l2.2-2.2c.3-.3.7-.4 1-.2 1.1.4 2.3.6 3.6.6.6 0 1 .4 1 1V20c0 .6-.4 1-1 1A17 17 0 0 1 3 4c0-.6.4-1 1-1h3.5c.6 0 1 .4 1 1 0 1.3.2 2.5.6 3.6.1.3 0 .7-.2 1z"/></svg>
      </span>
      OFFICE: 412.638.2940
    </li>
    <li>
      <span class="icon icon-direct">
        <svg width="16" height="16" viewBox="0 0 24 24"><path fill="#fff" d="M6.6 10.8a15 15 0 0 0 6.6 6.6l2.2-2.2c.3-.3.7-.4 1-.2 1.1.4 2.3.6 3.6.6.6 0 1 .4 1 1V20c0 .6-.4 1-1 1A17 17 0 0 1 3 4c0-.6.4-1 1-1h3.5c.6 0 1 .4 1 1 0 1.3.2 2.5.6 3.6.1.3 0 .7-.2 1z"/></svg>
      </span>
      DIRECT: 412.638.2957
    </li>
    <li>
      <span class="icon icon-fax">
        <svg width="16" height="16" viewBox="0 0 24 24"><path fill="#fff" d="M7 3h10v5H7zM4 9h16a1 1 0 0 1 1 1v7h-4v4H7v-4H3v-7a1 1 0 0 1 1-1zm5 7v3h6v-3z"/></svg>
      </span>
      412.638.2948
    </li>
  </ul>

  <div class="footer-bands">
    <span class="band-grey"></span>
    <span class="band-orange">
      <svg width="13" height="13" viewBox="0 0 24 24"><g fill="none" stroke="#fff" stroke-width="2"><circle cx="12" cy="12" r="10"/><path d="M2 12h20M12 2c3 3 3 17 0 20M12 2c-3 3-3 17 0 20"/></g></svg>
      VELDRAART.COM
    </span>
    <span class="band-gold"></span>
  </div>
  <div class="footer-rule"></div>
</section>

</body>
</html>
```